Square graphic for social media post

I want to create a 1080 x 1080px all-black image for the quote below that I can share on social media. I want the emphasis to be primarily on the quote, secondarily on the portrait, and third (smallest) on the logo. I want the background on the portrait to be edited so it's transparent and just shows the face of the person on a black background (no brick wall visible).

Graphic color: black
Text color: white
Content: "What we went through is going to make the greatest generation of hoteliers our industry has ever seen." << biggest text
Dorian Welk << smaller text
President, Marrowgate Hotels << smaller text
[image of person - use whichever version looks better to you]
[Add Lodging Ledger logo - whichever looks better to you]

This image needs to be readable when sized down much smaller (400x400?) so want the text and portrait to take up most of the space.

I'd like the output both as PNG and original file (preferably Canva). Thanks!

Target Market(s)

Hotel managers

Industry/Entity Type

Hospitality

Font styles to use
Sans Serif

Colors

Designer to choose colors to be used in the design.

Requirements
Must have
• Needs to focus on the quote and the person quoted (the portrait)

```html
<!DOCTYPE html>
<html lang="en">
<head>
<meta charset="utf-8">
<title>Quote Post – Dorian Welk</title>
<link rel="stylesheet" href="https://fonts.googleapis.com/css2?family=Roboto+Condensed:wght@400;500;700&family=Roboto:wght@400;500&family=Anton&display=swap">
<style>
  :root {
    --stage: #444444;
    --ink: #000000;
    --paper: #ffffff;
    --accent: #3b5ba6;
    --portrait-warm: #6b5650;
    --portrait-cool: #25355c;
  }
  * { margin: 0; padding: 0; box-sizing: border-box; }
  html, body {
    width: 675px; height: 1200px; overflow: hidden;
    background: var(--stage);
  }
  .post {
    position: absolute; left: 0; top: 262px;
    width: 675px; height: 675px;
    background: var(--ink);
    overflow: hidden;
    font-family: "Roboto Condensed", "Arial Narrow", sans-serif;
    color: var(--paper);
  }
  .portrait {
    position: absolute; left: 0; top: 0;
    width: 330px; height: 675px;
    background: linear-gradient(180deg, var(--ink) 0%, var(--portrait-warm) 30%, var(--portrait-warm) 60%, var(--portrait-cool) 100%);
  }
  .frame { position: absolute; left: 0; top: 0; width: 675px; height: 675px; }
  .quote-mark {
    position: absolute;
    font-family: "Anton", "Impact", sans-serif;
    font-size: 92px; line-height: 1;
    color: var(--paper);
  }
  .quote-mark--open { left: 337px; top: 10px; }
  .quote-mark--close { left: 619px; top: 586px; }
  .quote {
    position: absolute; right: 25px; top: 58px;
    width: 310px;
    text-align: right;
    font-weight: 500;
    font-size: 43px;
    line-height: 52.4px;
    text-transform: uppercase;
    letter-spacing: 0.2px;
  }
  .quote .highlight {
    background: var(--accent);
    padding: 2px 4px 2px 6px;
    margin-right: -4px;
  }
  .attribution {
    position: absolute; right: 34px; top: 492px;
    text-align: right;
    font-family: "Roboto", "Arial", sans-serif;
    font-size: 24px; line-height: 31px;
  }
  .speaker {
    position: absolute; right: 34px; top: 566px;
    display: flex; align-items: center; gap: 8px;
    font-family: "Roboto", "Arial", sans-serif;
    font-size: 22px; line-height: 32px;
    text-transform: uppercase;
  }
  .speaker__rule {
    display: block; width: 120px; height: 1px;
    background: var(--paper);
  }
</style>
</head>
<body>
  <main class="post">
    <div class="portrait" role="img" aria-label="Portrait photo of the quoted hotel president, smiling, in a white shirt and navy blazer, cut out on black"></div>

    <svg class="frame" viewBox="0 0 675 675" aria-hidden="true">
      <g stroke="var(--paper)" stroke-width="2" fill="none">
        <polyline points="344,461 344,49"/>
        <polyline points="384,49 659,49 659,605 484,605"/>
      </g>
    </svg>

    <span class="quote-mark quote-mark--open">“</span>

    <p class="quote">
      What we went<br>
      through is<br>
      going to make<br>
      <span class="highlight">the greatest</span><br>
      generation of<br>
      hoteliers our<br>
      industry has<br>
      ever seen.
    </p>

    <p class="attribution">President,<br>Marrowgate Hotels</p>
    <p class="speaker"><span class="speaker__rule"></span>Dorian Welk</p>

    <span class="quote-mark quote-mark--close">”</span>
  </main>
</body>
</html>
```